Enterprise IT illustration needs a twist and uniquness

The attached Powerpoint shows four conceptual houses that consist of 5 / 6 building blocks. We will build a lot of content around this concept and want a design that looks crisp, in line with our brand colors guideline and with logo/ copyright embedded. Each building blocks should have unique color aligned with brand guideline so that content can easily aligned with the specific building block (by color). Look for a clean, modern design with a twist. Need the files also in formats where I can change text if needed at a later point.

```html
<!DOCTYPE html>
<html lang="en">
<head>
<meta charset="utf-8">
<title>Hexagonal Building Blocks – Schemes</title>
<link href="https://fonts.googleapis.com/css2?family=Poppins:wght@400;600;700;800&display=swap" rel="stylesheet">
<style>
  :root{
    --yellow:#FFD800;
    --black:#231F20;
    --red:#FF4B5C;
    --navy:#263D8F;
    --cyan:#33E0FF;
    --orange:#F5A800;
    --grey:#858585;
    --white:#FFFFFF;
    --ink:#1E1E1E;
  }
  html,body{margin:0;padding:0;overflow:hidden;background:var(--yellow);}
  .canvas{width:797px;height:1200px;overflow:hidden;position:relative;background:var(--yellow);}
  .stage{position:absolute;left:0;top:0;width:1296px;height:1952px;transform:scale(0.615);transform-origin:0 0;font-family:'Poppins',sans-serif;}
  .stage svg{position:absolute;left:0;top:0;}
  .block-label{font-family:'Poppins',sans-serif;font-weight:700;font-size:30px;text-anchor:middle;}
  .block-num{font-family:'Poppins',sans-serif;font-weight:800;font-size:44px;text-anchor:middle;dominant-baseline:central;}
  .scheme-title{font-family:'Poppins',sans-serif;font-weight:800;font-size:46px;fill:var(--white);text-anchor:middle;dominant-baseline:central;letter-spacing:-0.5px;}
  .divider{position:absolute;left:0;top:975px;width:1296px;height:1px;background:var(--ink);}
  .notes{position:absolute;font-size:15px;line-height:17px;color:var(--ink);}
  .notes p{margin:0 0 12px;}
  .notes ul{margin:0;padding-left:18px;}
  .notes li{margin:0 0 12px;}
  .notes b{font-weight:700;}
  .notes-one{left:848px;top:606px;width:400px;}
  .notes-two{left:64px;top:1550px;width:340px;}
</style>
</head>
<body>
<div class="canvas">
<div class="stage">
<svg width="1296" height="1952" viewBox="0 0 1296 1952" xmlns="http://www.w3.org/2000/svg">
  <!-- Scheme 1 title -->
  <g class="scheme-badge">
    <polygon points="88,112 122,57 454,57 488,112 454,167 122,167" fill="#fff"/>
    <rect x="128" y="65" width="320" height="95" fill="#231F20"/>
    <text class="scheme-title" x="288" y="113">SCHEME 1</text>
  </g>

  <!-- Scheme 1 blocks -->
  <g class="block block-5">
    <polygon points="778,224 842,120 1076,120 1142,224 1076,328 842,328" fill="#231F20"/>
    <rect x="848" y="128" width="222" height="192" fill="#FF4B5C"/>
    <text class="block-num" x="820" y="224" fill="#FF4B5C">5</text>
    <text class="block-num" x="1097" y="224" fill="#FF4B5C">5</text>
    <text class="block-label" x="959" y="219" fill="#231F20">Taking<tspan x="959" dy="33">Action</tspan></text>
  </g>
  <g class="block block-4">
    <polygon points="468,336 534,232 768,232 834,336 768,440 534,440" fill="#263D8F"/>
    <rect x="540" y="240" width="222" height="192" fill="#fff"/>
    <text class="block-num" x="512" y="336" fill="#fff">4</text>
    <text class="block-num" x="789" y="336" fill="#fff">4</text>
    <text class="block-label" x="651" y="314" fill="#263D8F">Business<tspan x="651" dy="33">Relevant</tspan><tspan x="651" dy="33">Alerting</tspan></text>
  </g>
  <g class="block block-3">
    <polygon points="780,448 846,344 1080,344 1146,448 1080,552 846,552" fill="#33E0FF"/>
    <rect x="852" y="352" width="222" height="192" fill="#fff"/>
    <text class="block-num" x="828" y="448" fill="#fff">3</text>
    <text class="block-num" x="1099" y="448" fill="#fff">3</text>
    <text class="block-label" x="963" y="443" fill="#33E0FF">Topology<tspan x="963" dy="33">Discovery</tspan></text>
  </g>
  <g class="block block-2">
    <polygon points="468,560 534,456 768,456 834,560 768,664 534,664" fill="#F5A800"/>
    <rect x="540" y="464" width="222" height="192" fill="#fff"/>
    <text class="block-num" x="511" y="560" fill="#fff">2</text>
    <text class="block-num" x="787" y="560" fill="#fff">2</text>
    <text class="block-label" x="651" y="555" fill="#F5A800">Learn &amp;<tspan x="651" dy="33">Correlate</tspan></text>
  </g>
  <g class="block block-1">
    <polygon points="56,672 122,568 456,568 522,672 456,776 122,776" fill="#FF4B5C"/>
    <rect x="128" y="576" width="322" height="192" fill="#fff"/>
    <text class="block-num" x="104" y="677" fill="#fff">1</text>
    <text class="block-num" x="473" y="677" fill="#fff">1</text>
    <text class="block-label" x="289" y="667" fill="#FF4B5C">Quality Data<tspan x="289" dy="33">Harvesting</tspan></text>
  </g>

  <!-- Scheme 2 title -->
  <g class="scheme-badge">
    <polygon points="664,1088 698,1033 1030,1033 1064,1088 1030,1143 698,1143" fill="#fff"/>
    <rect x="704" y="1040" width="320" height="96" fill="#FF4B5C"/>
    <text class="scheme-title" x="864" y="1089">SCHEME 2</text>
  </g>

  <!-- Scheme 2 connectors -->
  <circle class="connector-ring" cx="842" cy="1412" r="140" fill="none" stroke="#858585" stroke-width="22"/>
  <polyline class="connector-path" points="289,1195 599,1308 599,1528 911,1636 599,1748" fill="none" stroke="#fff" stroke-width="26" stroke-linejoin="round"/>

  <!-- Scheme 2 blocks -->
  <g class="block block-5">
    <polygon points="106,1195 172,1091 406,1091 472,1195 406,1299 172,1299" fill="#231F20"/>
    <rect x="178" y="1099" width="222" height="192" fill="#fff"/>
    <text class="block-num" x="151" y="1195" fill="#fff">5</text>
    <text class="block-num" x="426" y="1195" fill="#fff">5</text>
    <text class="block-label" x="289" y="1190" fill="#231F20">Taking<tspan x="289" dy="33">Action</tspan></text>
  </g>
  <g class="block block-4">
    <polygon points="416,1308 482,1204 716,1204 782,1308 716,1412 482,1412" fill="#263D8F"/>
    <rect x="488" y="1212" width="222" height="192" fill="#fff"/>
    <text class="block-num" x="462" y="1308" fill="#fff">4</text>
    <text class="block-num" x="737" y="1308" fill="#fff">4</text>
    <text class="block-label" x="599" y="1286" fill="#263D8F">Business<tspan x="599" dy="33">Relevant</tspan><tspan x="599" dy="33">Alerting</tspan></text>
  </g>
  <g class="block block-extra">
    <polygon points="728,1416 794,1312 1028,1312 1094,1416 1028,1520 794,1520" fill="#fff"/>
    <rect x="800" y="1320" width="222" height="192" fill="#858585"/>
    <text class="block-num" x="772" y="1418" fill="#858585">+</text>
    <text class="block-num" x="1048" y="1414" fill="#858585">+</text>
    <text class="block-label" x="911" y="1427" fill="#fff" style="font-variant:small-caps;font-size:28px">Dashboards</text>
  </g>
  <g class="block block-3">
    <polygon points="416,1528 482,1424 716,1424 782,1528 716,1632 482,1632" fill="#33E0FF"/>
    <rect x="488" y="1432" width="222" height="192" fill="#fff"/>
    <text class="block-num" x="465" y="1528" fill="#fff">3</text>
    <text class="block-num" x="735" y="1528" fill="#fff">3</text>
    <text class="block-label" x="599" y="1523" fill="#33E0FF">Topology<tspan x="599" dy="33">Discovery</tspan></text>
  </g>
  <g class="block block-2">
    <polygon points="728,1636 794,1532 1028,1532 1094,1636 1028,1740 794,1740" fill="#F5A800"/>
    <rect x="800" y="1540" width="222" height="192" fill="#fff"/>
    <text class="block-num" x="771" y="1638" fill="#fff">2</text>
    <text class="block-num" x="1046" y="1636" fill="#fff">2</text>
    <text class="block-label" x="911" y="1631" fill="#F5A800">Learn &amp;<tspan x="911" dy="33">Correlate</tspan></text>
  </g>
  <g class="block block-1">
    <polygon points="416,1748 482,1644 716,1644 782,1748 716,1852 482,1852" fill="#FF4B5C"/>
    <rect x="488" y="1652" width="222" height="192" fill="#fff"/>
    <text class="block-num" x="461" y="1753" fill="#fff">1</text>
    <text class="block-num" x="733" y="1753" fill="#fff">1</text>
    <text class="block-label" x="599" y="1726" fill="#FF4B5C">Quality<tspan x="599" dy="33">Data</tspan><tspan x="599" dy="33">Harvesting</tspan></text>
  </g>
</svg>

<div class="divider"></div>

<div class="notes notes-one">
  <p><b>Hexagonal building blocks</b> allows for many different arrangements.</p>
  <ul>
    <li>You can easily create <b>linear structure</b> but also more <b>complex structure</b> where several blocks are touching, what can signify their connection.</li>
    <li>It's easy to <b>add an extra element</b> to the structure and simply rearrange the other elements.</li>
    <li>The <b>size of the block</b> can be easily enlarged by making the block wider to show importance of certain block (as is shown here with red Data block).</li>
    <li>It's also easy to <b>change colors</b> and color structure to emphasize it, see block 5 here.</li>
  </ul>
</div>

<div class="notes notes-two">
  <p><b>Extra building block</b> "+Dashboards" was added here to show another possible arrangement. Color scheme is different to show different weight of the block.</p>
  <ul>
    <li><b>Connection between block</b>s can be enhanced by underlying connectors - grey circle connecting blocks to the Dashboards block.</li>
    <li>In a similar way <b>path</b> can be also added behind connecting the main blocks (white line connecting blocks).</li>
  </ul>
</div>
</div>
</div>
</body>
</html>
```